Luxury Wine Label for New Startup Winery

We need a wine label for our new winery startup. We have worked with a local designer but do not feel the resulting label / logo have the elevation required to present our brand as a luxury wine. Our winery is called "Harrowgate Vineyards" and we are focused on extremely high quality hand crafted artisan and estate wines from the Pacific Northwest.
We would like to see designs that utilize a tree line, or other imagery that represents the "Harrowgate" part of our company name. Another interesting feature could be wood grain.
A logo will be required based on your design so please design with this in mind:
This logo should be consistent with the wine bottle label design, and should be representative of our high end exclusive wine while giving a sense of place (Oregon/ Pacific Northwest.)
I will supply an image of the design we received from our local designer, PLEASE NOTE: in general we do like wood grain and tree line concepts but feel the execution was poorly done.
ATTN: Logo design should be suitable for use on: Bottles (Red wine/rose/white wine), Bussiness cards, vehicle signage, business signage, etc
P.S.:
If you have a design that is not outside the box we are still interested in seeing it.
Label is for a burgundy style bottle with a label height of 3.5 - 4" and a width of 3.5-4"
any label <= 4"x4" and >=3.5"x3.5" will be acceptable:
HOWEVER Width should be greater than or equal to height due to the bottle format
Target Market(s)
Wine enthusiasts with adequate discretionary budgets to afford $100 bottles of wine.
Industry/Entity Type
Wine / Winery
Requirements
Must have
- A sense of luxury, a feel of exclusivity, and a theme consistent with our product and brand name
Nice to have
- Tree line, wood grain or other wood themes. Serif fonts
Should not have
- anything cheesy, off topic, hard to read script fonts or anything that makes the label hard to read from a few feet away or too busy

```html
<!DOCTYPE html>
<html lang="en">
<head>
<meta charset="utf-8">
<title>Harrowgate Vineyards – Syrah Label</title>
<link rel="stylesheet" href="https://fonts.googleapis.com/css2?family=Federo&family=Marcellus&display=swap">
<style>
  :root {
    --canvas: #ffffff;
    --label-black: #000000;
    --gold: #c7b35a;
    --gold-dark: #a8903e;
    --rule: #bfb8a0;
    --wood-light: #6e4a2c;
    --wood-dark: #4a2d17;
  }
  * { box-sizing: border-box; margin: 0; padding: 0; }
  html, body { width: 776px; height: 1200px; overflow: hidden; background: var(--canvas); }
  .canvas { position: relative; width: 776px; height: 1200px; }

  .label-set { position: absolute; width: 288px; }
  .label-set--sans { left: 190px; top: 145px; }
  .label-set--serif { left: 387px; top: 748px; }

  .front-label {
    position: relative;
    background: var(--label-black);
    color: var(--gold);
    text-align: center;
  }
  .label-set--sans .front-label { height: 233px; font-family: "Federo", sans-serif; }
  .label-set--serif .front-label { height: 212px; font-family: "Marcellus", serif; }

  .front-label__frame {
    position: absolute; inset: 17px;
    border: 1px solid var(--rule);
  }
  .tree-line {
    position: absolute; left: 30px; right: 30px; top: 10px; height: 70px;
    background: linear-gradient(180deg, rgba(199,179,90,0.15) 0%, var(--gold-dark) 75%, var(--gold) 100%);
    clip-path: polygon(0 70%, 100% 40%, 100% 100%, 0 100%);
  }
  .label-set--serif .tree-line { top: 14px; height: 66px; }

  .winery-name {
    position: absolute; left: 0; right: 0;
    font-weight: 400; line-height: 1; letter-spacing: 0.02em;
  }
  .label-set--sans .winery-name { top: 94px; font-size: 27px; }
  .label-set--serif .winery-name { top: 96px; font-size: 25px; }
  .winery-name span { display: block; }
  .winery-name span + span { margin-top: 2px; letter-spacing: 0.12em; }

  .region {
    position: absolute; left: 68px; right: 68px;
    border-top: 1px solid var(--gold-dark);
    border-bottom: 1px solid var(--gold-dark);
    font-size: 14px; line-height: 1; padding: 5px 0 6px; letter-spacing: 0.03em;
  }
  .label-set--sans .region { top: 160px; }
  .label-set--serif .region { top: 160px; left: 40px; right: 40px; font-size: 15px; }

  .vintage-line {
    position: absolute; left: 0; right: 0;
    font-size: 11px; letter-spacing: 0.06em; line-height: 1;
  }
  .label-set--sans .vintage-line { top: 197px; }
  .label-set--serif .vintage-line { top: 196px; font-size: 12px; }

  .varietal-band {
    position: relative; height: 61px; margin-top: 10px;
  }
  .label-set--serif .varietal-band { margin-top: 32px; }
  .wood-grain {
    position: absolute; inset: 0;
    background: linear-gradient(90deg, var(--wood-dark), var(--wood-light) 30%, var(--wood-dark) 60%, var(--wood-light) 85%, var(--wood-dark));
  }
  .varietal-band__frame {
    position: absolute; left: 15px; right: 17px; top: 16px; bottom: 17px;
    border: 1px solid var(--gold);
    display: flex; align-items: center; justify-content: center;
  }
  .varietal {
    color: var(--gold); font-size: 20px; letter-spacing: 0.06em; line-height: 1;
  }
  .label-set--sans .varietal { font-family: "Federo", sans-serif; }
  .label-set--serif .varietal { font-family: "Marcellus", serif; }
</style>
</head>
<body>
<main class="canvas">
  <section class="label-set label-set--sans">
    <div class="front-label">
      <div class="tree-line" role="img" aria-label="Gold evergreen tree line illustration"></div>
      <div class="front-label__frame"></div>
      <h1 class="winery-name"><span>HARROWGATE</span><span>VINEYARDS</span></h1>
      <p class="region">WILLAMETTE VALLEY</p>
      <p class="vintage-line">ESTATE | 2023 | GROWN</p>
    </div>
    <div class="varietal-band">
      <div class="wood-grain" role="img" aria-label="Walnut wood grain texture"></div>
      <div class="varietal-band__frame"><span class="varietal">SYRAH</span></div>
    </div>
  </section>

  <section class="label-set label-set--serif">
    <div class="front-label">
      <div class="tree-line" role="img" aria-label="Gold evergreen tree line illustration"></div>
      <div class="front-label__frame"></div>
      <h2 class="winery-name"><span>HARROWGATE</span><span>VINEYARDS</span></h2>
      <p class="region">WILLAMETTE VALLEY</p>
      <p class="vintage-line">ESTATE | 2023 | GROWN</p>
    </div>
    <div class="varietal-band">
      <div class="wood-grain" role="img" aria-label="Walnut wood grain texture"></div>
      <div class="varietal-band__frame"><span class="varietal">SYRAH</span></div>
    </div>
  </section>
</main>
</body>
</html>
```